Dravel

We are openıng one huntıng showroom in Riyadh? Saudi Arabia. Company name is "DRAVEL".
Our logo designed and we need Business Card Design now.
I attached DRAVEL logo below.
Front side will English and back side will be Arabic

```html
<!DOCTYPE html>
<html lang="en">
<head>
<meta charset="utf-8">
<title>Dravel Business Card</title>
<link href="https://fonts.googleapis.com/css2?family=Michroma&family=Jura:wght@600;700&family=Cairo:wght@700&display=swap" rel="stylesheet">
<style>
  :root {
    --stage: #1d1d1d;
    --brand-green: #0a8a52;
    --leaf-green: #5a9e3c;
    --card-white: #ffffff;
    --mist: #efe9d6;
    --olive: #8f845a;
    --olive-deep: #4f4526;
    --text-light: #ffffff;
  }
  * { box-sizing: border-box; margin: 0; padding: 0; }
  html, body { width: 1200px; height: 1200px; overflow: hidden; }
  body {
    background: var(--stage);
    display: flex; flex-direction: column; align-items: center; justify-content: center;
    gap: 56px;
  }
  .card {
    position: relative;
    width: 900px; height: 514px;
    border-radius: 34px;
    overflow: hidden;
    background: var(--card-white);
  }
  .card__scene {
    position: absolute; inset: 0;
    background:
      linear-gradient(180deg, rgba(255,255,255,0) 0%, rgba(255,255,255,0) 30%, var(--mist) 48%, var(--olive) 72%, var(--olive-deep) 100%),
      linear-gradient(90deg, rgba(60,50,25,0.35) 0%, rgba(60,50,25,0) 45%);
    background-color: var(--card-white);
  }
  .name-block { position: absolute; top: 40px; left: 40px; }
  .name-block__name {
    font-family: "Michroma", sans-serif;
    color: var(--brand-green);
    font-size: 32px; line-height: 1;
    padding-left: 18px;
  }
  .name-block__title {
    margin-top: 6px;
    background: var(--leaf-green);
    color: var(--text-light);
    font-family: "Jura", sans-serif; font-weight: 700;
    font-size: 24px; line-height: 1;
    padding: 5px 16px 6px;
  }
  .brand {
    position: absolute; top: 135px; right: 60px;
    display: flex; align-items: center; gap: 16px;
  }
  .brand__mark { width: 26px; height: 26px; background: var(--brand-green); }
  .brand__name {
    font-family: "Michroma", sans-serif;
    color: var(--brand-green);
    font-size: 72px; line-height: 1;
  }
  .contacts {
    position: absolute; left: 40px; bottom: 70px;
    list-style: none;
    font-family: "Jura", sans-serif; font-weight: 700;
    color: var(--text-light);
    font-size: 30px; line-height: 1;
  }
  .contacts li { display: flex; align-items: center; gap: 14px; margin-top: 8px; }
  .contacts__icon {
    width: 28px; height: 28px; background: var(--leaf-green);
    display: flex; align-items: center; justify-content: center; flex: none;
  }
  .location {
    position: absolute; right: 60px; bottom: 44px;
    font-family: "Jura", sans-serif; font-weight: 700;
    color: var(--text-light); font-size: 30px; line-height: 1.2;
  }
  .card--arabic .name-block__name,
  .card--arabic .name-block__title,
  .card--arabic .location { font-family: "Cairo", sans-serif; direction: rtl; }
  .card--arabic .name-block__name { font-size: 38px; }
  .card--arabic .name-block__title { font-size: 22px; padding: 2px 16px 4px; }
  .card--arabic .location { font-size: 20px; bottom: 26px; }
</style>
</head>
<body>

  <section class="card card--arabic" lang="ar">
    <div class="card__scene" role="img" aria-label="Hunting scene: silhouetted hunters aiming shotguns at flying birds over grassy hills"></div>
    <div class="name-block">
      <p class="name-block__name">اسمك</p>
      <p class="name-block__title">المدير العام</p>
    </div>
    <div class="brand"><span class="brand__mark"></span><span class="brand__name">DRAVEL</span></div>
    <ul class="contacts">
      <li><span class="contacts__icon"><svg width="18" height="18" viewBox="0 0 24 24"><path fill="#fff" d="M6.6 10.8a15 15 0 0 0 6.6 6.6l2.2-2.2c.3-.3.7-.4 1-.2 1.1.4 2.3.6 3.6.6.6 0 1 .4 1 1V20c0 .6-.4 1-1 1A17 17 0 0 1 3 4c0-.6.4-1 1-1h3.5c.6 0 1 .4 1 1 0 1.3.2 2.5.6 3.6.1.3 0 .7-.2 1z"/></svg></span>214-555-0184</li>
      <li><span class="contacts__icon"><svg width="18" height="14" viewBox="0 0 24 18"><rect x="1" y="1" width="22" height="16" fill="none" stroke="#fff" stroke-width="2"/><path d="M1 1l11 9 11-9" fill="none" stroke="#fff" stroke-width="2"/></svg></span>info@dravel.com</li>
      <li><span class="contacts__icon"><svg width="18" height="18" viewBox="0 0 24 24" fill="none" stroke="#fff" stroke-width="1.8"><circle cx="12" cy="12" r="10"/><ellipse cx="12" cy="12" rx="4.5" ry="10"/><path d="M2 12h20M4 6.5h16M4 17.5h16"/></svg></span>www.yourwebsitehere.com</li>
    </ul>
    <p class="location">الرياض، المملكة العربية السعودية</p>
  </section>

  <section class="card card--english">
    <div class="card__scene" role="img" aria-label="Hunting scene: silhouetted hunters aiming shotguns at flying birds over grassy hills"></div>
    <div class="name-block">
      <p class="name-block__name">YOUR NAME</p>
      <p class="name-block__title">Managing Director</p>
    </div>
    <div class="brand"><span class="brand__mark"></span><span class="brand__name">DRAVEL</span></div>
    <ul class="contacts">
      <li><span class="contacts__icon"><svg width="18" height="18" viewBox="0 0 24 24"><path fill="#fff" d="M6.6 10.8a15 15 0 0 0 6.6 6.6l2.2-2.2c.3-.3.7-.4 1-.2 1.1.4 2.3.6 3.6.6.6 0 1 .4 1 1V20c0 .6-.4 1-1 1A17 17 0 0 1 3 4c0-.6.4-1 1-1h3.5c.6 0 1 .4 1 1 0 1.3.2 2.5.6 3.6.1.3 0 .7-.2 1z"/></svg></span>214-555-0184</li>
      <li><span class="contacts__icon"><svg width="18" height="14" viewBox="0 0 24 18"><rect x="1" y="1" width="22" height="16" fill="none" stroke="#fff" stroke-width="2"/><path d="M1 1l11 9 11-9" fill="none" stroke="#fff" stroke-width="2"/></svg></span>info@dravel.com</li>
      <li><span class="contacts__icon"><svg width="18" height="18" viewBox="0 0 24 24" fill="none" stroke="#fff" stroke-width="1.8"><circle cx="12" cy="12" r="10"/><ellipse cx="12" cy="12" rx="4.5" ry="10"/><path d="M2 12h20M4 6.5h16M4 17.5h16"/></svg></span>www.yourwebsitehere.com</li>
    </ul>
    <p class="location">Riyadh, Saudi Arabia</p>
  </section>

</body>
</html>
```